Business Cards for IT Consulting Company (Managed Service Provider)

I am looking to have some business cards printed and would like some designs. We are an IT Consulting company based in Vancouver BC. I would like a nice clean and modern look to the cards. I have uploaded all the versions of my logo so parts can be used as needed. Here is a snippit from our website homepage:

Kelbrook Systems Ltd. is an IT Solutions Partner located in Vancouver BC, Canada. We offer IT solutions and support to customers in the greater Vancouver Area. With expertise in Microsoft platforms, as well as Linux and Mac OSX and over 12 years experience in the IT industry, Kelbrook Systems is dedicated to offering our clients top quality service and products. We take pride in the solutions we offer our customers. The greatest compliment a client can give us is to recommend our services.

Kelbrook Systems Ltd. offers a wide range of IT services from onsite service to remote support and managed service solutions. This allows clients to choose the support path that best suits their company’s needs. Supporting many different sized companies from small to enterprise level over the past 12 years Kelbrook Systems has the experience and expertise needed to ensure things run smoothly. Allowing our clients to focus on doing business.

Revolutionizing the way IT services are delivered.

Kelbrook Systems is dedicated to providing our clients with IT solutions that work and grow with them for years to come. This philosophy helps save money in the long run instead of replacing equipment constantly. Far too often IT solutions are not well thought out and while possibly solving the problem at hand, require replacement due to growth or quality within a very short time frame. Kelbrook Systems takes pride in providing solutions that will last and be able to accommodate growth without the need for replacement.

Industry/Entity Type

Information Technology

Contact Information for Business Card

Kelbrook Systems Ltd.
(Employee Name)
Eml: (Employees Email Address)
Web: kelbrook.me
Ph: 604-555-0142

Font styles to use
Serif
Sans Serif

Requirements
Must have
• The Company logo and company colors.
Nice to have
• - Our tag line: "Revolutionizing IT Services" or "Revolutionizing the way IT services are delivered."
• - Also I really like the idea of nature and technology together blending which is sort of where my logo came from so integrating that somehow onto the business cards would be great.

```html
<!DOCTYPE html>
<html lang="en">
<head>
<meta charset="utf-8">
<title>Kelbrook Systems Ltd. – Business Cards</title>
<link rel="stylesheet" href="https://fonts.googleapis.com/css2?family=Raleway:wght@300;400&display=swap">
<style>
  :root {
    --bg: #c4e6dc;
    --card-black: #050505;
    --brand-blue: #0a9ad8;
    --muted-grey: #6b6b6b;
    --paper-white: #ffffff;
    --text-white: #f2f2f2;
  }
  * { margin: 0; padding: 0; box-sizing: border-box; }
  html, body { width: 1200px; height: 856px; overflow: hidden; }
  body {
    background: var(--bg);
    font-family: "Raleway", sans-serif;
    position: relative;
  }
  .card {
    position: absolute;
    width: 560px;
    height: 320px;
    border-radius: 26px;
    background: var(--card-black);
    overflow: hidden;
    box-shadow: 0 14px 30px rgba(0, 60, 50, 0.18);
  }
  .card--back { left: 560px; top: 80px; }
  .card--front { left: 90px; top: 440px; }

  /* Company name, set as plain text */
  .company {
    display: flex;
    align-items: center;
  }
  .company-dot {
    border-radius: 50%;
    background: var(--brand-blue);
    flex: none;
  }
  .company-name {
    color: var(--text-white);
    font-weight: 400;
    letter-spacing: 0.5px;
    white-space: nowrap;
  }

  /* Back side */
  .card--back .company {
    position: absolute;
    left: 60px;
    top: 80px;
    gap: 16px;
  }
  .card--back .company-dot { width: 20px; height: 20px; }
  .card--back .company-name { font-size: 32px; }
  .tagline {
    position: absolute;
    left: 100px;
    top: 196px;
    font-size: 30px;
    font-weight: 400;
    letter-spacing: 0.5px;
    white-space: nowrap;
  }
  .tagline__lead { color: var(--brand-blue); }
  .tagline__rest { color: var(--muted-grey); }

  /* Front side */
  .feature-panel {
    position: absolute;
    inset: 0;
    background: var(--paper-white);
    clip-path: polygon(0 0, 30% 0, 42% 100%, 0 100%);
  }
  .feature-edge {
    position: absolute;
    inset: 0;
    width: 100%;
    height: 100%;
  }
  .front-info {
    position: absolute;
    left: 270px;
    top: 36px;
    right: 16px;
  }
  .card--front .company { gap: 10px; }
  .card--front .company-dot { width: 13px; height: 13px; }
  .card--front .company-name { font-size: 20px; }
  .person-name {
    margin-top: 38px;
    color: var(--brand-blue);
    font-weight: 300;
    font-size: 32px;
    letter-spacing: 1.5px;
    text-transform: uppercase;
    white-space: nowrap;
  }
  .contact-list {
    list-style: none;
    margin-top: 20px;
  }
  .contact-item {
    display: flex;
    align-items: center;
    gap: 12px;
    color: var(--text-white);
    font-size: 18px;
    height: 36px;
    white-space: nowrap;
  }
  .contact-icon {
    width: 26px;
    height: 26px;
    border-radius: 50%;
    background: var(--brand-blue);
    display: flex;
    align-items: center;
    justify-content: center;
    flex: none;
  }
  .contact-icon svg { width: 15px; height: 15px; }
</style>
</head>
<body>

  <section class="card card--back" aria-label="Card back">
    <div class="company">
      <span class="company-dot"></span>
      <span class="company-name">Kelbrook Systems Ltd.</span>
    </div>
    <p class="tagline">
      <span class="tagline__lead">Revolutionizing</span>
      <span class="tagline__rest">IT Services</span>
    </p>
  </section>

  <section class="card card--front" aria-label="Card front">
    <div class="feature-panel" role="img" aria-label="Large brand decoration area in white with blue accents"></div>
    <svg class="feature-edge" viewBox="0 0 560 320" aria-hidden="true">
      <line x1="168" y1="0" x2="235" y2="320" stroke="var(--brand-blue)" stroke-width="7"/>
    </svg>

    <div class="front-info">
      <div class="company">
        <span class="company-dot"></span>
        <span class="company-name">Kelbrook Systems Ltd.</span>
      </div>
      <h1 class="person-name">Daniel Hart</h1>
      <ul class="contact-list">
        <li class="contact-item">
          <span class="contact-icon">
            <svg viewBox="0 0 24 24"><path fill="#fff" d="M6.6 10.8a15.1 15.1 0 0 0 6.6 6.6l2.2-2.2a1 1 0 0 1 1-.25 11.4 11.4 0 0 0 3.6.57 1 1 0 0 1 1 1V20a1 1 0 0 1-1 1A17 17 0 0 1 3 4a1 1 0 0 1 1-1h3.5a1 1 0 0 1 1 1c0 1.25.2 2.45.57 3.6a1 1 0 0 1-.25 1z"/></svg>
          </span>
          daniel.hart@kelbrook.me
        </li>
        <li class="contact-item">
          <span class="contact-icon">
            <svg viewBox="0 0 24 24"><rect x="3" y="6" width="18" height="12" rx="1.5" fill="#fff"/><path d="M3.5 6.5 12 13l8.5-6.5" fill="none" stroke="#0a9ad8" stroke-width="1.6"/></svg>
          </span>
          kelbrook.me
        </li>
        <li class="contact-item">
          <span class="contact-icon">
            <svg viewBox="0 0 24 24" fill="none" stroke="#fff" stroke-width="1.8"><circle cx="12" cy="12" r="9"/><ellipse cx="12" cy="12" rx="4" ry="9"/><line x1="3" y1="12" x2="21" y2="12"/></svg>
          </span>
          604-555-0142
        </li>
      </ul>
    </div>
  </section>

</body>
</html>
```